Business card design needed

This is a roofing company that specialises in metal roofs on period homes. I want to market to the more affluent areas in Melbourne as they are very expensive homes and period style. If you look at period homes in Melbourne you will see the metal roofs with ornate guttering and lattice work. An image of a roof or part of it would look good on the card - as it will catch the eye of the home owner in my view.

I dont have a logo so feel free to do what you want. I am open to all ideas and will choose the most appropriate.

I want to make the card look very professional and upmarket. Most roofers just use cards made cheaply, so this is my opportunity to differentiate from those. I dont want a cheap looking card. Must really look professional and make the home owner think I am very good at what I do.

I am going to put these cards in letter boxes to market my business. As this has worked before.

A good example of period homes with the roofs I work on are:
http://www.tindlebrookhouses.com.au/Tindlebrook-Houses-photo-gallery.html
Please check out the houses in the gallery. If I can get the message across with a beautiful photo of a roof - the home owner will be enticed to call me based on the image. I believe the image of the period home roof - or part of - will make a difference. As most of my competitors just have a sketch or words.

I will be making a quality card that is thick and printed in high resolution.

Target Market(s)

Home owners who are most likely tertiary educated and high income earners.

Industry/Entity Type

Roofing

Contact Information for Business Card

Mr Dean Pellowe
Professional Roofing Expert (est 30 years)
No obligation appraisal
Licensed. Quality. Guaranteed.

Mobile: 0438 726 913
Fax: 9587 3046
Email: crestlinetiles.vic@quillmail.com

On the back of the card can you put.....
Metal Roofing Specialists
Quality Period Home Experience
New and Old Roofing Expertise
Roof Maintenance and Repair
Over 30 years experience
References Provided
Polite and Punctual

Requirements
Nice to have
• I am open to all ideas. Layout and design is up to you. Go for it.

```html
<!DOCTYPE html>
<html lang="en">
<head>
<meta charset="utf-8">
<title>Crestline Roofing – Business Card</title>
<link rel="stylesheet" href="https://fonts.googleapis.com/css2?family=Fira+Sans:wght@500;600;700&family=Fira+Sans+Condensed:wght@300;600&display=swap">
<style>
  :root {
    --ink-blue: #1634c4;
    --roof-red: #b5103a;
    --name-grey: #363f42;
    --fresh-green: #5bd420;
    --lime-light: #eef23c;
    --lime-mid: #c8ea3a;
    --lime-deep: #9ade3c;
    --paper: #ffffff;
    --text-dark: #222222;
  }
  * { margin: 0; padding: 0; box-sizing: border-box; }
  html, body {
    width: 1200px; height: 741px; overflow: hidden;
    background: var(--paper);
  }
  .card {
    position: relative; width: 1200px; height: 741px;
    background: var(--paper); overflow: hidden;
    font-family: "Fira Sans", Arial, sans-serif;
  }
  .wave { position: absolute; inset: 0; }

  .owner-name {
    position: absolute; right: 32px; top: 60px;
    font-size: 40px; font-weight: 700; letter-spacing: 1.5px;
    color: var(--name-grey);
  }

  .brand {
    position: absolute; left: 40px; top: 178px; width: 792px;
  }
  .brand-name {
    font-size: 104px; font-weight: 700; letter-spacing: -1px;
    line-height: 1; color: var(--ink-blue); white-space: nowrap;
  }
  .brand-footer {
    display: flex; justify-content: space-between; align-items: flex-end;
    margin-top: 14px;
  }
  .brand-tagline {
    margin-left: 131px;
    font-size: 30px; font-weight: 600; line-height: 1.2;
    color: var(--ink-blue); text-align: center;
  }
  .established {
    font-size: 38px; font-weight: 500; line-height: 1;
    color: var(--fresh-green);
    text-shadow: 1px 2px 2px rgba(0,0,0,0.35);
  }

  .appraisal-offer {
    position: absolute; left: 952px; top: 462px;
    transform: rotate(20deg); transform-origin: center;
    font-size: 29px; font-weight: 600; line-height: 1.05;
    color: var(--roof-red); text-align: center; letter-spacing: 1px;
  }
  .promise {
    position: absolute; left: 0; right: 10px; top: 572px;
    text-align: center;
    font-size: 39px; font-weight: 600; letter-spacing: 2px;
    color: var(--ink-blue);
  }
  .contact-line {
    position: absolute; left: 0; right: 0; top: 676px;
    text-align: center;
    font-family: "Fira Sans Condensed", "Arial Narrow", sans-serif;
    font-size: 32px; font-weight: 300; color: var(--text-dark);
    white-space: nowrap;
  }
  .contact-line strong { font-weight: 600; }
</style>
</head>
<body>
<div class="card">
  <svg class="wave" width="1200" height="741" viewBox="0 0 1200 741" aria-hidden="true">
    <defs>
      <linearGradient id="lime-field" x1="0" y1="0" x2="1" y2="1">
        <stop offset="0" stop-color="var(--lime-light)"/>
        <stop offset="0.55" stop-color="var(--lime-mid)"/>
        <stop offset="1" stop-color="var(--lime-deep)"/>
      </linearGradient>
    </defs>
    <path d="M0,427 C180,470 330,548 530,534 C720,518 900,405 1200,388 L1200,741 L0,741 Z" fill="url(#lime-field)"/>
  </svg>

  <div class="owner-name">Dean Pellowe</div>

  <div class="brand">
    <div class="brand-name">Crestline Roofing</div>
    <div class="brand-footer">
      <div class="brand-tagline">PROFESSIONAL<br>SERVICES</div>
      <div class="established">Est 30 years</div>
    </div>
  </div>

  <div class="appraisal-offer">No Obligation<br>APPRAISAL</div>

  <div class="promise">LICENSED - QUALITY - GUARANTEED</div>

  <div class="contact-line">
    Mobile: <strong>0438 726 913</strong> Fax: <strong>9587 3046</strong> Email: <strong>crestlinetiles.vic@quillmail.com</strong>
  </div>
</div>
</body>
</html>
```